Business Card Design for Event Planning Company

Create a business card for event planning company using our new logo. After I pick the design, I will need files made for 6 employees. Our company provides event design & logistics services as well as venue management. The font should be sans serif and complementary to the logo. I will need to know the name of the font selected for the final design. The phone numbers listed should be separated by "." not "-"

Address for the card
PO Box 318, Washington, DC 20019

Card One
Lorna Pettibone
lpettibone@galavoyant.com
202.481.7730

Card Two
Miriam Okonkwo
mokonkwo@galavoyant.com
202.556.2047

Card Three
Tessa Varnholt
tvarnholt@galavoyant.com
978.620.4471

Card Four
Robin Fess
rfess@galavoyant.com
202.718.3362

Card Five
Ada-Rose Pelletan-Uzor
adarose@galavoyant.com
202.839.1205

Card Six
Beatrix Holloway
Beatrix@galavoyant.com
202.492.6618

Target Market(s)

Corporate/Non-Profit

Industry/Entity Type

Event Planning

Contact Information for Business Card

Address for the card

Card One
Lorna Pettibone
lpettibone@galavoyant.com
202.481.7730

Card Two
Miriam Okonkwo
202.556.2047

Card Three
Tessa Varnholt
978.620.4471

Card Four
Robin Fess
rfess@galavoyant.com
202.718.3362

Card Five
Ada-Rose Pelletan-Uzor
202.839.1205

Card Six
Beatrix Holloway
202.492.6618

Font styles to use
Sans Serif

Colors

Designer to choose colors to be used in the design.

Requirements
Must have
• Two-sided with logo
Should not have
• Extra colors or be too busy

```html
<!DOCTYPE html>
<html lang="en">
<head>
<meta charset="utf-8">
<title>Galavoyant Business Card</title>
<link rel="stylesheet" href="https://fonts.googleapis.com/css2?family=Questrial&family=Arimo:wght@400&display=swap">
<style>
  :root {
    --backdrop: #e3e4e6;
    --teal: #5bb5b1;
    --teal-deep: #47a29e;
    --ink: #2b2b2b;
    --ink-soft: #4a4a4a;
    --paper: #ffffff;
  }
  * { margin: 0; padding: 0; box-sizing: border-box; }
  html, body {
    width: 1200px; height: 800px; overflow: hidden;
    background: var(--backdrop);
  }
  .canvas { position: relative; width: 1200px; height: 800px; }
  .card {
    position: absolute; top: 252px;
    width: 520px; height: 297px;
    box-shadow: 0 6px 18px rgba(0,0,0,0.12);
  }
  .card--front {
    left: 50px;
    background: linear-gradient(135deg, var(--teal-deep), var(--teal) 60%, #68c0bc);
  }
  .card--back { left: 630px; background: var(--paper); }

  .wordmark {
    position: absolute; display: flex; align-items: center; gap: 12px;
    font-family: "Questrial", sans-serif; letter-spacing: 0.5px;
  }
  .card--front .wordmark {
    left: 0; right: 0; top: 118px; justify-content: center;
    color: var(--paper); font-size: 50px;
  }
  .wordmark__dot {
    width: 36px; height: 36px; border-radius: 50%;
    border: 3px solid currentColor;
  }
  .card--back .wordmark {
    left: 30px; top: 92px; color: var(--teal); font-size: 34px; gap: 9px;
  }
  .card--back .wordmark__dot { width: 24px; height: 24px; border-width: 2px; }

  .divider {
    position: absolute; left: 278px; top: 60px;
    width: 1.5px; height: 150px; background: var(--teal);
  }
  .contact {
    position: absolute; left: 300px; top: 82px;
    font-family: "Arimo", sans-serif; color: var(--ink-soft);
  }
  .contact__name {
    font-family: "Questrial", sans-serif; color: var(--ink);
    font-size: 20px; letter-spacing: 0.6px; text-transform: uppercase;
    margin-bottom: 10px;
  }
  .contact__row {
    display: flex; align-items: center; gap: 7px;
    font-size: 12.5px; margin-bottom: 7px; white-space: nowrap;
  }
  .contact__icon { width: 15px; height: 15px; flex: none; }

  .address {
    position: absolute; left: 30px; top: 222px;
    font-family: "Arimo", sans-serif; color: var(--ink);
    font-size: 12.5px; line-height: 1.35;
  }
</style>
</head>
<body>
<main class="canvas">
  <section class="card card--front" aria-label="Card front">
    <div class="wordmark"><span class="wordmark__dot"></span>galavoyant</div>
  </section>

  <section class="card card--back" aria-label="Card back">
    <div class="wordmark"><span class="wordmark__dot"></span>galavoyant</div>
    <div class="divider"></div>
    <div class="contact">
      <p class="contact__name">Lorna Pettibone</p>
      <p class="contact__row">
        <svg class="contact__icon" viewBox="0 0 16 16" aria-hidden="true">
          <circle cx="8" cy="8" r="7.2" fill="none" stroke="var(--teal)" stroke-width="1.2"/>
          <rect x="4.3" y="5.3" width="7.4" height="5.4" fill="none" stroke="var(--ink-soft)" stroke-width="1"/>
          <path d="M4.3 5.3 L8 8.3 L11.7 5.3" fill="none" stroke="var(--ink-soft)" stroke-width="1"/>
        </svg>
        lpettibone@galavoyant.com
      </p>
      <p class="contact__row">
        <svg class="contact__icon" viewBox="0 0 16 16" aria-hidden="true">
          <circle cx="8" cy="8" r="7.2" fill="none" stroke="var(--teal)" stroke-width="1.2"/>
          <rect x="5.6" y="3.8" width="4.8" height="8.4" rx="0.8" fill="none" stroke="var(--ink-soft)" stroke-width="1"/>
          <line x1="7.3" y1="10.8" x2="8.7" y2="10.8" stroke="var(--ink-soft)" stroke-width="0.9"/>
        </svg>
        202.481.7730
      </p>
    </div>
    <p class="address">Address for the card<br>PO Box 318, Washington, DC 20019</p>
  </section>
</main>
</body>
</html>
```